Tree Pruning Website

We need a website for a tree Arborist, pruning company called Hollow Ridge Groundcare. We look after all types of trees, knock down trees and prune trees. Our target market is from domestic clients to government clients and everything in between.

We would like to see the use of our main colours which are orange and green

We are not looking forward in seeing a template that we have seen before but a unique template. We have designed 5 templates ourselves and we wish for the design community to take our designs to the next level.

We have also designed a template for things that **we are not** looking for (Version 4)

To make it fair for everyone, we are also not giving out any participation payments as we have had. One winner will take all of the payment!!!

I Have attached a image of the designs and a image of a tree.

We are just looking at the PSD file been developed. We have our own team who can slice the image up into a HTML format.

Target Market(s)

Everyone who needs to cut down a tree

Industry/Entity Type

Government

Requirements
Must have
• Logo on front page
A List of our services
jQuery slider on page
Phone Number on every page

```html
<!DOCTYPE html>
<html lang="en">
<head>
<meta charset="utf-8">
<title>Hollow Ridge Groundcare</title>
<link href="https://fonts.googleapis.com/css2?family=Didact+Gothic&display=swap" rel="stylesheet">
<style>
:root{
  --green:#8cc63f;
  --green-dark:#6a9a1f;
  --orange:#f7941d;
  --ink:#555;
  --ink-soft:#8a8a8a;
  --rule:#e4e4e4;
  --top-bar:#4a1414;
  --white:#fff;
}
*{margin:0;padding:0;box-sizing:border-box}
html,body{width:1200px;height:1044px;overflow:hidden;background:var(--white)}
body{font-family:"Didact Gothic",Arial,sans-serif;color:var(--ink);position:relative;border-top:2px solid var(--top-bar)}
a{text-decoration:none;color:inherit}

.site-header{position:absolute;top:0;left:0;width:1200px;height:88px}
.brand{position:absolute;left:123px;top:42px;font-size:20px;font-weight:700;color:var(--green-dark);letter-spacing:.2px;display:flex;align-items:center;gap:8px}
.brand-dot{width:10px;height:10px;border-radius:50%;background:var(--orange)}
.main-nav{position:absolute;right:123px;top:41px;display:flex;gap:0}
.main-nav a{font-size:15px;color:#777;padding:3px 15.5px;border-radius:4px;line-height:18px}
.main-nav a.current{background:var(--green);color:var(--white);margin-right:4px}

.hero{position:absolute;top:88px;left:0;width:1200px;height:375px;
  background:linear-gradient(180deg,#d9a63a 0%,#c9b27a 25%,#a2ab88 45%,#6f8a3c 65%,#5e7c24 100%)}
.hero-glow{position:absolute;inset:0;background:radial-gradient(circle at 840px 140px,rgba(255,246,200,.75),rgba(255,246,200,0) 260px),
  radial-gradient(ellipse at 120px 60px,rgba(222,140,20,.7),rgba(222,140,20,0) 300px)}
.hero-product{position:absolute;left:712px;top:180px;width:366px;height:195px;border-radius:40px 40px 0 0;
  background:linear-gradient(180deg,#9bd23a 0%,#5d6d2e 55%,#6e4a2a 100%);opacity:.85}
.hero-title{position:absolute;left:121px;top:260px;font-size:36px;line-height:38px;color:var(--white);font-weight:400;letter-spacing:.3px}
.slider-dots{position:absolute;left:124px;top:351px;display:flex;gap:4px}
.slider-dots span{width:10px;height:10px;border-radius:50%;background:var(--orange)}
.slider-dots span.active{background:var(--white)}

.sectors{position:absolute;top:498px;left:0;width:1200px}
.sector{position:absolute;width:220px;text-align:center}
.sector-icon{width:54px;height:52px;margin:0 auto;border-radius:6px}
.sector h3{font-size:22px;font-weight:400;color:#555;margin-top:12px;letter-spacing:.5px}
.sector p{font-size:12px;line-height:16.5px;color:var(--ink-soft);margin-top:8px}
.learn-more{display:inline-block;font-size:12px;color:var(--green-dark);border-bottom:1px dotted var(--green-dark);line-height:14px;margin-top:2px}

.divider-shadow{position:absolute;top:694px;left:123px;width:954px;height:14px;
  background:radial-gradient(ellipse at 50% 0,rgba(0,0,0,.08),rgba(0,0,0,0) 70%)}

.about{position:absolute;top:742px;left:123px;width:690px}
.section-title{font-size:22px;font-weight:400;color:#555;letter-spacing:.3px}
.about-lead{margin-top:20px;font-size:13px;color:var(--orange);text-decoration:underline;text-underline-offset:2px}
.about p.body{font-size:11.5px;line-height:17px;color:var(--ink-soft);margin-top:14px}
.about p.body + p.body{margin-top:17px}
.about .learn-more{margin-top:10px}

.services{position:absolute;top:742px;left:868px;width:210px}
.service-list{list-style:none;margin-top:22px}
.service-list li{display:flex;align-items:center;gap:15px;font-size:12px;color:#777;height:20.3px}
.service-list li::before{content:"";width:12px;height:12px;border:2.5px solid var(--orange);border-radius:50%}

.footer-rule{position:absolute;top:983px;height:1px;background:var(--rule)}
.footer-rule.left{left:123px;width:430px}
.footer-rule.right{left:643px;width:434px}
.site-footer{position:absolute;top:1005px;left:123px;width:954px;font-size:12px;color:var(--ink-soft);display:flex;justify-content:space-between}
.site-footer strong{color:#555;font-weight:400}
.legal a{margin:0 4px}
</style>
</head>
<body>
<header class="site-header">
  <a class="brand" href="#"><span class="brand-dot"></span>Hollow Ridge Groundcare</a>
  <nav class="main-nav">
    <a class="current" href="#">Home</a>
    <a href="#">About Us</a>
    <a href="#">Our Services</a>
    <a href="#">Gat a Quote</a>
    <a href="#">Our Works</a>
    <a href="#">Contact Us</a>
  </nav>
</header>

<section class="hero">
  <div class="hero-glow" role="img" aria-label="Autumn trees over a sunlit green valley"></div>
  <div class="hero-product" role="img" aria-label="Green chainsaw and work gloves resting on a tree stump"></div>
  <h1 class="hero-title">Lorem ipsum dolor sit amet,<br>consectetur adipiscing elit.</h1>
  <div class="slider-dots"><span></span><span></span><span class="active"></span><span></span></div>
</section>

<section class="sectors">
  <div class="sector" style="left:113px">
    <div class="sector-icon" role="img" aria-label="House icon" style="background:linear-gradient(#d9531e 45%,#f1e3c8 45%)"></div>
    <h3>Domestic</h3>
    <p>Lorem ipsum dolor sit amet, consectetur adipiscing elit. Curabitur nec enim ut quam luctus ornare. Integer dictum,</p>
    <a class="learn-more" href="#">Learn More &gt;</a>
  </div>
  <div class="sector" style="left:366px">
    <div class="sector-icon" role="img" aria-label="Commercial building icon" style="background:linear-gradient(#8a5a36 45%,#ded6cb 45%)"></div>
    <h3>Commercial</h3>
    <p>Lorem ipsum dolor sit amet, consectetur adipiscing elit. Curabitur nec enim ut quam luctus ornare. Integer dictum,</p>
    <a class="learn-more" href="#">Learn More &gt;</a>
  </div>
  <div class="sector" style="left:615px">
    <div class="sector-icon" role="img" aria-label="Tree and park bench icon" style="background:linear-gradient(#4f8a1e 60%,#c8c2b4 60%);border-radius:50% 50% 6px 6px"></div>
    <h3>Goverment</h3>
    <p>Lorem ipsum dolor sit amet, consectetur adipiscing elit. Curabitur nec enim ut quam luctus ornare. Integer dictum,</p>
    <a class="learn-more" href="#">Learn More &gt;</a>
  </div>
  <div class="sector" style="left:863px">
    <div class="sector-icon" role="img" aria-label="Piggy bank icon" style="background:radial-gradient(circle at 50% 60%,#f7b417 55%,transparent 57%)"></div>
    <h3>Non Profit</h3>
    <p>Lorem ipsum dolor sit amet, consectetur adipiscing elit. Curabitur nec enim ut quam luctus ornare. Integer dictum,</p>
    <a class="learn-more" href="#">Learn More &gt;</a>
  </div>
</section>

<div class="divider-shadow"></div>

<section class="about">
  <h2 class="section-title">About Us</h2>
  <p class="about-lead">Lorem ipsum dolor sit amet, consectetur adipiscing elit.</p>
  <p class="body">Lorem ipsum dolor sit amet, consectetur adipiscing elit. Curabitur nec enim ut quam luctus ornare. Integer dictum, dolor vel fermentum ullamcorper dolor purus sagittis sapien, quis dignissim metus purus id purus. Donec id quam sem, eu suscipit tellus.</p>
  <p class="body">Donec vitae mi ut leo porta consequat sit amet eget turpis. Pellentesque eu dapibus nisl. Quisque vitae sagittis ligula. Nullam volutpat arcu nec leo posuere posuere id eu enim. Fusce pulvinar metus sagittis quam mollis lacinia. Cum sociis natoque penatibus et magnis dis parturient montes, na scetur ridiculus us Sed ac tortor sem. Aliquam erat volutpat.</p>
  <a class="learn-more" href="#">Learn More &gt;</a>
</section>

<aside class="services">
  <h2 class="section-title">Our Services</h2>
  <ul class="service-list">
    <li>Diagnosis</li>
    <li>Treatment</li>
    <li>Purning</li>
    <li>Tree Removal</li>
    <li>Stump Removal</li>
    <li>Cabling &amp; Bracing</li>
    <li>Arborist Consults</li>
    <li>Tree Protection</li>
  </ul>
</aside>

<div class="footer-rule left"></div>
<div class="footer-rule right"></div>
<footer class="site-footer">
  <span>Copyright&copy; 2012 <strong>Hollow Ridge Groundcare</strong> . All Rights Reserved</span>
  <span class="legal"><a href="#">Privacy Policy</a> | <a href="#">Term of Use</a></span>
</footer>
</body>
</html>
```